Bright Fern Painting needs a new business card. See attachments for our logo and current card as an example.
We want to utilize the same colors in the logo, and keep all the information that is currently on it. Just need an updated and modern design.
We are open to loosing the Association Logos if it means a better design.
We are also entertaining a spot for a picture of a headshot of the person listed on the card. Head shot can be finished later.

```html
<!DOCTYPE html>
<html lang="en">
<head>
<meta charset="utf-8">
<title>Bright Fern Painting – Business Card</title>
<link href="https://fonts.googleapis.com/css2?family=Open+Sans:wght@400;600;700&display=swap" rel="stylesheet">
<style>
  :root {
    --stage: #2b2b2b;
    --fern-green: #434d35;
    --fern-green-dark: #3a4330;
    --brick: #6b3a37;
    --paper: #ffffff;
    --ink: #4a4a4a;
  }
  * { margin: 0; padding: 0; box-sizing: border-box; }
  html, body { width: 1200px; height: 892px; overflow: hidden; }
  body {
    background: var(--stage);
    font-family: "Open Sans", Arial, sans-serif;
    position: relative;
  }
  .card {
    position: absolute;
    width: 560px;
    height: 320px;
    box-shadow: 0 12px 30px rgba(0,0,0,.45);
  }

  /* Front */
  .card-front {
    left: 70px; top: 90px;
    background: linear-gradient(160deg, var(--fern-green), var(--fern-green-dark));
    color: var(--paper);
  }
  .front-brand {
    position: absolute;
    top: 100px; left: 0; right: 0;
    text-align: center;
    font-weight: 600;
    font-size: 34px;
    letter-spacing: 2px;
    line-height: 1.2;
  }
  .front-services {
    position: absolute;
    left: 30px; bottom: 34px;
    font-size: 12.5px;
    letter-spacing: .5px;
    text-transform: uppercase;
  }

  /* Back */
  .card-back {
    left: 570px; top: 470px;
    background: var(--paper);
    color: var(--ink);
  }
  .name-band {
    position: absolute;
    left: 0; top: 92px;
    width: 100%; height: 50px;
    background: var(--brick);
    border-bottom: 6px solid var(--fern-green);
    padding: 6px 0 0 40px;
    color: var(--paper);
  }
  .person-name { font-weight: 700; font-size: 17px; letter-spacing: .5px; line-height: 1.15; }
  .person-role { font-size: 13px; letter-spacing: .5px; line-height: 1.2; }
  .back-brand {
    position: absolute;
    right: 22px; top: 26px;
    background: var(--paper);
    padding: 8px 12px;
    display: flex; align-items: center; gap: 10px;
    font-weight: 600;
    font-size: 20px;
    letter-spacing: 1px;
    color: var(--fern-green);
    line-height: 1.1;
    text-align: right;
  }
  .brand-square { width: 14px; height: 14px; background: var(--brick); flex: none; }
  .website {
    position: absolute;
    right: 30px; top: 172px;
    font-size: 13px; letter-spacing: .8px;
  }
  .contact-list {
    position: absolute;
    left: 40px; bottom: 30px;
    list-style: none;
    font-size: 14px;
    letter-spacing: .4px;
  }
  .contact-list li { display: flex; align-items: center; gap: 10px; line-height: 1.5; }
  .contact-list svg { width: 14px; height: 14px; fill: var(--fern-green); flex: none; }
</style>
</head>
<body>

  <section class="card card-front">
    <div class="front-brand">BRIGHT FERN<br>PAINTING</div>
    <p class="front-services">Exterior Painting • Interior Painting • Carpentry • Drywell</p>
  </section>

  <section class="card card-back">
    <div class="name-band">
      <div class="person-name">MARK DALTON</div>
      <div class="person-role">QUALITY MANAGER</div>
    </div>
    <div class="back-brand">
      <span class="brand-square"></span>
      <span>BRIGHT FERN<br>PAINTING</span>
    </div>
    <p class="website">www.brightfernpainting.com</p>
    <ul class="contact-list">
      <li>
        <svg viewBox="0 0 24 24" aria-hidden="true"><path d="M6.6 10.8a15.1 15.1 0 0 0 6.6 6.6l2.2-2.2a1 1 0 0 1 1-.25 11.4 11.4 0 0 0 3.6.57 1 1 0 0 1 1 1V20a1 1 0 0 1-1 1A17 17 0 0 1 3 4a1 1 0 0 1 1-1h3.5a1 1 0 0 1 1 1c0 1.25.2 2.45.57 3.57a1 1 0 0 1-.25 1z"/></svg>
        262-555-0148
      </li>
      <li>
        <svg viewBox="0 0 24 24" aria-hidden="true"><path d="M2 5h20v14H2z M2 5l10 8 10-8" stroke="#fff" stroke-width="1.5"/></svg>
        mark@brightfernpainting.com
      </li>
    </ul>
  </section>

</body>
</html>
```